Wordpress Design Project (Varnet)

We need a wordpress design for an established auction and real estate company based in Pennsylvania. The winning design will incorporate a professional layout with and company logo in a very simple and clean layout.

Industry/Entity Type

Real Estate

Requirements
Must have
• Navigation:
1) Home; 2) Auctions; 3) Appraisals; 4) Real Estate; 5) FAQ; 6) About Us; 7) Contact Us.

Site will have overall layout of https://www.plimtova.com/featured/regions/the-northeast. Home page will have logo and navigation at top. The navigation bar will also have social media icons (facebook, Google+, RSS, twitter) inside it. There will be text in the content area - use lorem ipsum. The image attached will be used below text (auctions.jpg) . Footer will have smaller company loogo, the attached affiliation logos and social media icons.

Logo attached. Color scheme will be black, gray, and red as accent color.
Nice to have
• navigation will have dropdowns, nice to have one represented - under auctions 'All Auctions' will be dropdown.

```html
<!DOCTYPE html>
<html lang="en">
<head>
<meta charset="utf-8">
<title>Varnet Auctioneers &amp; Appraisers</title>
<link href="https://fonts.googleapis.com/css2?family=Questrial&family=Arimo:wght@400&display=swap" rel="stylesheet">
<style>
  :root {
    --red: #c8100f;
    --red-deep: #a20a0a;
    --red-bright: #e31b17;
    --ink: #2b2b2b;
    --muted: #555555;
    --page: #f4f3f4;
    --line: #e2e2e2;
    --footer: #1f1f1f;
    --footer-text: #d6d6d6;
    --white: #ffffff;
  }
  * { box-sizing: border-box; margin: 0; padding: 0; }
  html, body { width: 1013px; height: 1200px; overflow: hidden; }
  body {
    position: relative;
    background: var(--page);
    font-family: "Questrial", Arial, sans-serif;
    color: var(--ink);
  }
  .site-header {
    position: absolute; left: 0; top: 0; width: 1013px; height: 127px;
    background: linear-gradient(100deg, #dcdcdc 0%, #f3f3f3 45%, #ffffff 70%, #ececec 100%);
    border-top: 4px solid #cfcfcf;
  }
  .brand {
    position: absolute; left: 62px; top: 20px; width: 280px; height: 88px;
    background: var(--white); border: 1px solid #d8d8d8;
    box-shadow: 0 1px 3px rgba(0,0,0,.15);
    display: flex; align-items: center; gap: 14px; padding-left: 14px;
  }
  .brand-mark { width: 68px; height: 68px; background: var(--red); border-radius: 4px; }
  .brand-name { font-size: 40px; color: #111; letter-spacing: 1px; }
  .connect { position: absolute; right: 65px; top: 26px; text-align: right; }
  .connect-title { font-size: 17px; color: #333; margin-bottom: 8px; }
  .social { display: flex; gap: 8px; justify-content: flex-end; }
  .social span { width: 33px; height: 33px; border-radius: 3px; display: block; }
  .social .s1 { background: #3b5aa0; }
  .social .s2 { background: #37b4e6; }
  .social .s3 { background: #7fb03b; }
  .social .s4 { background: #f07a22; }
  .main-nav {
    position: absolute; left: 0; top: 131px; width: 1013px; height: 44px;
    background: #f8f8f8;
    border-top: 1px dashed #c9c9c9; border-bottom: 2px solid #d4d4d4;
  }
  .main-nav ul { list-style: none; display: flex; height: 100%; align-items: center; }
  .main-nav li { position: absolute; top: 12px; font-size: 17px; color: #2a2a2a; }
  .main-nav li.active { color: var(--red); }
  .main-nav li.active::before {
    content: ""; position: absolute; left: 50%; top: -13px; margin-left: -5px;
    border: 5px solid transparent; border-top-color: var(--red);
  }
  .hero-frame {
    position: absolute; left: 53px; top: 209px; width: 907px; height: 290px;
    background: #ececec;
  }
  .hero {
    position: absolute; left: 60px; top: 219px; width: 893px; height: 272px;
    background: radial-gradient(ellipse at 55% 20%, var(--red-bright) 0%, var(--red) 50%, var(--red-deep) 100%);
    border: 2px dashed rgba(255,255,255,.85);
    color: var(--white); text-align: center;
  }
  .hero-title {
    font-size: 30px; font-weight: 400; margin: 20px 30px 0;
    padding-bottom: 6px; border-bottom: 1px dashed rgba(255,255,255,.7);
  }
  .hero-text { font-size: 14px; line-height: 21.3px; margin: 24px 34px 0; }
  .listing { position: absolute; width: 391px; text-align: center; }
  .listing-photo {
    display: block; width: 391px; height: 187px;
    background: var(--white); padding: 4px; border: 1px solid #dcdcdc;
  }
  .listing-photo span { display: block; width: 100%; height: 100%; }
  .listing-title { font-size: 20px; color: var(--red); margin-top: 10px; font-weight: 400; }
  .listing-sub { font-size: 14.5px; color: var(--muted); margin-top: 3px; letter-spacing: .3px; }
  .listing-date { font-size: 12.5px; color: #444; margin-top: 4px; letter-spacing: .5px; }
  .row-divider { position: absolute; left: 78px; top: 800px; width: 853px; border-top: 1px solid var(--line); }
  .site-footer {
    position: absolute; left: 0; top: 1100px; width: 1013px; height: 100px;
    background: var(--footer); border-top: 4px solid #3a3a3a;
    font-family: "Arimo", Arial, sans-serif; color: var(--footer-text);
  }
  .footer-mark { position: absolute; left: 71px; top: 20px; width: 48px; height: 49px; background: #8a8a8a; border-radius: 4px; }
  .footer-links { position: absolute; left: 131px; top: 32px; font-size: 12px; word-spacing: 2px; }
  .footer-links span { color: #9a9a9a; margin: 0 6px; }
  .copyright { position: absolute; left: 131px; top: 57px; font-size: 12px; }
  .affiliations { position: absolute; left: 782px; top: 12px; width: 162px; height: 75px; }
</style>
</head>
<body>
  <header class="site-header">
    <div class="brand">
      <span class="brand-mark"></span>
      <span class="brand-name">Varnet</span>
    </div>
    <div class="connect">
      <div class="connect-title">Get Connected</div>
      <div class="social" aria-label="Social links">
        <span class="s1"></span><span class="s2"></span><span class="s3"></span><span class="s4"></span>
      </div>
    </div>
  </header>

  <nav class="main-nav">
    <ul>
      <li class="active" style="left:81px">Home</li>
      <li style="left:190px">Auctions</li>
      <li style="left:319px">Appraisals</li>
      <li style="left:466px">Real Estate</li>
      <li style="left:616px">FAQ</li>
      <li style="left:710px">About Us</li>
      <li style="left:843px">Contact Us</li>
    </ul>
  </nav>

  <div class="hero-frame"></div>
  <section class="hero">
    <h1 class="hero-title">Lorem ipsum dolor sit amet, consectetuer adipiscing elit</h1>
    <p class="hero-text">Nullam enim leo, egestas id, condimentum at, laoreet mattis, massa. Sed eleifend nonummy diam. Praesent mauris ante, elementum et, bibendum at, posuere sit amet, nibh. Duis tincidunt lectus quis dui viverra vestibulum. Suspendisse vulputate aliquam dui. Nulla elementum dui ut augue. Aliquam vehicula mi at mauris. Maecenas placerat, nisl at consequat rhoncus, sem nunc gravida justo, quis eleifend arcu velit quis lacus. Morbi magna magna, tincidunt a, mattis non, imperdiet vitae, tellus. Sed odio est, auctor ac, sollicitudin in, consequat vitae, orci. Fusce id felis. Vivamus sollicitudin metus eget eros. Pellentesque habitant morbi tristique senectus et netus et malesuada fames ac turpis egestas</p>
  </section>

  <article class="listing" style="left:78px;top:531px">
    <div class="listing-photo"><span role="img" aria-label="Row of white paneled doors in a warehouse" style="background:linear-gradient(90deg,#6f7a86,#a9b2bb 50%,#8f8a78)"></span></div>
    <h2 class="listing-title">Mauris vel lacus vitae</h2>
    <p class="listing-sub">Etiam est nunc, venenatis in</p>
    <p class="listing-date">Dated: 12-08-13</p>
  </article>
  <article class="listing" style="left:540px;top:531px">
    <div class="listing-photo"><span role="img" aria-label="Stacked carpet rolls with yellow tags" style="background:linear-gradient(135deg,#8a857a,#b9b2a3 50%,#7e8387)"></span></div>
    <h2 class="listing-title">Mauris vel lacus vitae</h2>
    <p class="listing-sub">Etiam est nunc, venenatis in</p>
    <p class="listing-date">Dated: 12-08-13</p>
  </article>

  <div class="row-divider"></div>

  <article class="listing" style="left:78px;top:817px">
    <div class="listing-photo"><span role="img" aria-label="Wooden cabinets lined up in a warehouse" style="background:linear-gradient(90deg,#8a5a3c,#5a2424 45%,#7a6a5a)"></span></div>
    <h2 class="listing-title">Mauris vel lacus vitae</h2>
    <p class="listing-sub">Etiam est nunc, venenatis in</p>
    <p class="listing-date">Dated: 12-08-13</p>
  </article>
  <article class="listing" style="left:540px;top:817px">
    <div class="listing-photo"><span role="img" aria-label="Wooden bathroom vanities with stone tops" style="background:linear-gradient(180deg,#a58a76,#3a3330 35%,#9a5a2c)"></span></div>
    <h2 class="listing-title">Mauris vel lacus vitae</h2>
    <p class="listing-sub">Etiam est nunc, venenatis in</p>
    <p class="listing-date">Dated: 12-08-13</p>
  </article>

  <footer class="site-footer">
    <span class="footer-mark"></span>
    <div class="footer-links">Home<span>|</span>Auctions<span>|</span>Appraisals<span>|</span>Real Estate<span>|</span>FAQ<span>|</span>About Us<span>|</span>Contact Us</div>
    <div class="copyright">Copyright © Varnet Auctioneers &amp; Appraisers.</div>
    <svg class="affiliations" viewBox="0 0 162 75" aria-label="Affiliation badges">
      <g fill="#8f8f8f">
        <rect x="0" y="4" width="28" height="28" rx="2"/>
        <circle cx="72" cy="18" r="16"/>
        <circle cx="136" cy="18" r="15"/>
        <rect x="0" y="44" width="28" height="28" rx="2"/>
        <rect x="58" y="44" width="28" height="28" rx="2"/>
        <circle cx="136" cy="58" r="15"/>
      </g>
    </svg>
  </footer>
</body>
</html>
```